NEED LABEL FOR PACKAGED DRINKING WATER BOTTLE

we are a new company who is into manufacturing of packaged drinking water bottles in 200 ml 500 ml and 1000 ml. we already have a label which we are using in our local market but we are introducing our 200ml bottle in inflight catering where our products will be seen, consumed by various age and origin of people who travel on flights. so we want a label which is simple and elegant.the bottle is a square bottle and label size would be 198 mm x 36 mm.you can use the label provided below for reference.and the bottle shape also is provided
Target Market(s)
flight passengers in domestic flights
Industry/Entity Type
It Company
Look and feel

```html
<!DOCTYPE html>
<html lang="en">
<head>
<meta charset="utf-8">
<title>Aquora Packaged Drinking Water – 200 ml Label</title>
<link href="https://fonts.googleapis.com/css2?family=Arimo:ital,wght@0,400;0,700;1,700&display=swap" rel="stylesheet">
<style>
  :root{
    --page:#ffffff;
    --cyan:#27c6f2;
    --cyan-light:#6fe0fb;
    --blue:#1c5fc4;
    --blue-deep:#0d3d9e;
    --yellow:#fcd116;
    --gold:#f5b400;
    --white:#ffffff;
    --ink:#0b1f55;
  }
  *{margin:0;padding:0;box-sizing:border-box}
  html,body{width:927px;height:1200px;overflow:hidden;background:var(--page)}
  body{font-family:"Arimo",Arial,sans-serif;position:relative}
  .label{
    position:absolute;left:0;top:45px;width:927px;height:173px;
    background:linear-gradient(180deg,var(--cyan-light) 0%,var(--cyan) 45%,var(--cyan) 100%);
    border-top:4px solid var(--yellow);border-bottom:4px solid var(--yellow);
    overflow:hidden;color:var(--white);
  }
  .label__waves{position:absolute;inset:0;width:100%;height:100%}
  .panel{position:absolute;top:0;bottom:0}
  .info{left:26px;top:10px;width:170px;font-weight:700}
  .info__qty{color:var(--yellow);font-size:10.5px}
  .info__qty small{font-size:6px;font-weight:400}
  .info__codes{display:flex;align-items:center;margin-top:3px;color:var(--yellow);font-size:6.5px;line-height:1.15}
  .info__brace{font-size:22px;font-weight:400;margin:0 4px;line-height:1}
  .info__see{color:var(--white);font-size:7.5px;text-align:center}
  .info__cert{display:flex;justify-content:space-between;align-items:flex-end;margin-top:6px;font-size:7px;line-height:1.25}
  .badge{width:26px;height:18px;border:1.5px solid var(--white);border-radius:2px}
  .info__care{margin-top:7px;color:var(--yellow);font-size:5.6px;line-height:1.25}
  .info__foot{display:flex;align-items:center;gap:4px;margin-top:6px}
  .dot{width:14px;height:14px;border-radius:50%;background:var(--yellow)}
  .crush{background:var(--yellow);color:var(--ink);font-size:7px;padding:2px 5px;border-radius:8px}
  .info__tiny{display:flex;justify-content:space-between;font-size:5px;font-weight:400;margin-top:2px;width:170px}
  .brand{display:flex;flex-direction:column;align-items:center;justify-content:center;width:170px}
  .brand--front{left:250px}
  .brand--back{left:735px}
  .brand__name{font-size:40px;font-weight:700;color:var(--blue-deep);line-height:1}
  .brand__rule{width:120px;height:3px;background:var(--blue-deep);margin:4px 0 3px}
  .brand__tag{font-size:10px;font-style:italic;font-weight:700;color:var(--blue-deep)}
  .story{left:500px;width:185px;top:12px;text-align:center;font-weight:700;font-size:7.4px;line-height:1.4}
  .story__title{display:inline-block;background:var(--yellow);color:var(--ink);padding:1px 6px;border-radius:8px;font-size:7px;margin-bottom:4px}
  .story__text{color:var(--yellow)}
  .story__maker{margin-top:5px;color:var(--white)}
  .story__care{margin-top:6px;color:var(--yellow);font-weight:400}
  .vertical{position:absolute;left:660px;top:118px;transform:rotate(-90deg);transform-origin:left top;font-size:4.5px;color:var(--white)}
</style>
</head>
<body>
  <section class="label" aria-label="Aquora 200 ml bottle wrap label">
    <svg class="label__waves" viewBox="0 0 927 165" preserveAspectRatio="none" aria-hidden="true">
      <path d="M0 95 C200 60 330 150 520 120 C680 95 780 60 927 90 L927 165 L0 165Z" fill="#1c8be0" opacity=".55"/>
      <path d="M230 165 C330 120 430 120 520 135 C640 155 760 110 927 125 L927 165Z" fill="#1c5fc4"/>
      <path d="M210 40 C320 10 420 90 500 70" stroke="#ffffff" stroke-width="2" fill="none" opacity=".6"/>
      <path d="M690 30 C760 10 840 60 927 40" stroke="#ffffff" stroke-width="2" fill="none" opacity=".6"/>
    </svg>

    <div class="panel info">
      <p class="info__qty">Net Quantity : 1ℓ <small>( when pkd )</small></p>
      <div class="info__codes">
        <p>MFG. DATE<br>BATCH NO.<br>M.R.P. <span style="font-size:4.5px">(INCL.Of All Taxes)</span></p>
        <span class="info__brace">}</span>
        <p class="info__see">See Neck /<br>Bottle</p>
      </div>
      <div class="info__cert">
        <p>For quality certification details<br>see website : www.qualitymark.org</p>
        <div class="badge" role="img" aria-label="Certification badge"></div>
      </div>
      <p class="info__care">Best Before Six Months From Manufacture<br>Store In Cool And Dry Hygienic Conditions<br>Do Not Buy If Seal/cap Is Broken</p>
      <div class="info__foot">
        <div class="dot" role="img" aria-label="Recycle icon"></div>
        <span class="crush">Crush the Bottle After Use</span>
        <div class="dot" role="img" aria-label="Keep city clean icon"></div>
      </div>
      <div class="info__tiny"><span>Recyclable</span><span>200 ml</span><span>Keep your city clean</span></div>
    </div>

    <div class="panel brand brand--front">
      <p class="brand__name">Aquora</p>
      <div class="brand__rule"></div>
      <p class="brand__tag">Packaged Drinking Water</p>
    </div>

    <div class="panel story">
      <p class="story__title">PACKAGED DRINKING WATER</p>
      <p class="story__text">Every bottle of Aquora is put through our state-of-art process that comprises of Sand Filtration, Activated Carbon Filtration, Reverse Osmosis, UV treatment and Ozonisation. Packed under stringent hygienic condition</p>
      <p class="story__maker">Mfg. And Pkd By:<br>M/s. Brightwell Beverages,<br>Plot No. 12/B,<br>Riverside Industrial Estate,<br>Lakeview, Sundernagar - 500999</p>
      <p class="story__care">For suggestions and complaints call<br>Customer Care No : +91 9000012345</p>
    </div>
    <p class="vertical">PRINTED LABEL</p>

    <div class="panel brand brand--back">
      <p class="brand__name">Aquora</p>
      <div class="brand__rule"></div>
      <p class="brand__tag">Packaged Drinking Water</p>
    </div>
  </section>
</body>
</html>
```